Need Eye Catching For Sale By Owner Signs

In need of a Eye Catching For Sale By Owner Sign design. I plan on using the sign to market buildings and raw land that I own. The design should be able to scale to different rectangular dimensions for example a yard stake sign or a large 4' x 6' sign to be tacked to plywood. The design should have a dead space near the bottom that I can insert more detail information into at a later time.

The main tag line "For Sale By Owner" and the contact number "318-562-4097" needs to be easily be read from a distance.

```html
<!DOCTYPE html>
<html lang="en">
<head>
<meta charset="utf-8">
<title>For Sale By Owner Sign</title>
<link rel="stylesheet" href="https://fonts.googleapis.com/css2?family=Poppins:wght@600&family=Nunito:wght@800&display=swap">
<style>
  :root {
    --sign-white: #ffffff;
    --sign-blue: #3a89c9;
    --sign-charcoal: #555658;
  }
  html, body {
    margin: 0;
    padding: 0;
    overflow: hidden;
    background: var(--sign-white);
  }
  .sign {
    display: block;
    width: 1200px;
    height: 800px;
    overflow: hidden;
    background: var(--sign-white);
  }
  .info-band { fill: var(--sign-blue); }
  .headline {
    font-family: "Poppins", sans-serif;
    font-weight: 600;
    font-size: 229px;
    fill: var(--sign-charcoal);
  }
  .subline {
    font-family: "Poppins", sans-serif;
    font-weight: 600;
    font-size: 120px;
    fill: var(--sign-blue);
  }
  .phone {
    font-family: "Nunito", sans-serif;
    font-weight: 800;
    font-size: 125px;
    fill: var(--sign-white);
  }
  .chevron-upper { fill: var(--sign-blue); }
  .chevron-lower { fill: var(--sign-white); }
</style>
</head>
<body>
  <svg class="sign" width="1200" height="800" viewBox="0 0 1200 800" role="img" aria-label="For sale by owner, call 318.562.4097">
    <rect class="info-band" x="0" y="398" width="1200" height="402"/>

    <text class="headline" x="78" y="255" textLength="1042" lengthAdjust="spacingAndGlyphs">FOR SALE</text>
    <text class="subline" x="80" y="366" textLength="648" lengthAdjust="spacingAndGlyphs">BY OWNER</text>
    <text class="phone" x="78" y="520" textLength="650" lengthAdjust="spacingAndGlyphs">318.562.4097</text>

    <g class="chevrons">
      <g>
        <polygon class="chevron-upper" points="815,282 870,282 988,400 933,400"/>
        <polygon class="chevron-lower" points="933,400 988,400 870,520 815,520"/>
      </g>
      <g transform="translate(89 0)">
        <polygon class="chevron-upper" points="815,282 870,282 988,400 933,400"/>
        <polygon class="chevron-lower" points="933,400 988,400 870,520 815,520"/>
      </g>
      <g transform="translate(178 0)">
        <polygon class="chevron-upper" points="815,282 870,282 988,400 933,400"/>
        <polygon class="chevron-lower" points="933,400 988,400 870,520 815,520"/>
      </g>
      <g transform="translate(267 0)">
        <polygon class="chevron-upper" points="815,282 870,282 988,400 933,400"/>
        <polygon class="chevron-lower" points="933,400 988,400 870,520 815,520"/>
      </g>
    </g>
  </svg>
</body>
</html>
```